Bright Fern Custom Homes business card. Double sided. Modern. professional

Bright Fern Custom Homes
contemporary modern design with our logo /
Double sided with all our contact information
Use same Green colors as in our Logo. Contemporary logo that grabs your attention. Visually pleasing and balanced. Easy to read, and Vibrant. Would love an option for rounded edges. Embossed logo would be amazing.
Contact Information for Business Card
Dana Welk Owner / General Contractor Bright Fern Custom Homes p: 704.552.1830 m: 912.648.2071 e: brightferncustomhomes@mailbox.example w: www.brightferncustomhomes.example 218 Pryor Meadow Lane Batesburg, SC 29041

```html
<!DOCTYPE html>
<html lang="en">
<head>
<meta charset="utf-8">
<title>Bright Fern Custom Homes – Business Card</title>
<link rel="stylesheet" href="https://fonts.googleapis.com/css2?family=Ubuntu:wght@400;500&display=swap">
<style>
  :root {
    --bg: #dcdde1;
    --card: #ffffff;
    --green: #5f7f2c;
    --green-dark: #3f5a1f;
    --green-light: #7a9a3c;
    --ink: #5a5a5a;
  }
  * { margin: 0; padding: 0; box-sizing: border-box; }
  html, body { width: 1200px; height: 824px; overflow: hidden; background: var(--bg); }
  body { position: relative; font-family: "Ubuntu", Arial, sans-serif; color: var(--ink); }

  .card {
    position: absolute;
    left: 385px;
    width: 430px;
    height: 245px;
    background: var(--card);
    border-radius: 10px;
    overflow: hidden;
  }
  .card--front { top: 136px; }
  .card--back { top: 443px; }

  /* Front */
  .brand {
    position: absolute;
    left: 0; right: 0;
    top: 106px;
    display: flex;
    align-items: center;
    justify-content: center;
    gap: 8px;
  }
  .brand__dot { width: 12px; height: 12px; border-radius: 50%; background: var(--green); }
  .brand__name { font-size: 19px; font-weight: 400; color: var(--green); letter-spacing: 0.5px; }

  /* Back */
  .card__art {
    position: absolute;
    left: 0; top: 0;
    width: 213px; height: 245px;
    background: linear-gradient(160deg, var(--green-light) 0%, var(--green) 50%, var(--green-dark) 100%);
    clip-path: polygon(0 0, 60% 0, 100% 70%, 100% 76%, 55% 100%, 0 100%);
  }
  .person {
    position: absolute;
    left: 215px; top: 39px;
    border-left: 3px solid var(--green);
    padding-left: 5px;
  }
  .person__name { font-size: 25px; line-height: 24px; font-weight: 400; color: var(--ink); }
  .person__name strong { font-weight: 500; }
  .person__role { font-size: 15px; line-height: 18px; color: var(--green); margin-top: 2px; }

  .contact { position: absolute; left: 215px; font-size: 10.2px; line-height: 12.6px; color: var(--ink); }
  .contact--address { top: 117px; }
  .contact--lines { top: 160px; }
  .contact__row { display: flex; align-items: flex-start; gap: 3px; white-space: nowrap; }
  .contact__icon { width: 9px; height: 9px; margin-top: 2px; flex: none; fill: none; stroke: var(--green); stroke-width: 1.4; }
  .contact__icon--solid { fill: var(--green); stroke: none; }
  .contact__indent { padding-left: 0; }
</style>
</head>
<body>

<section class="card card--front" aria-label="Card front">
  <div class="brand">
    <span class="brand__dot"></span>
    <span class="brand__name">Bright Fern Custom Homes</span>
  </div>
</section>

<section class="card card--back" aria-label="Card back">
  <div class="card__art" role="img" aria-label="Large green brand illustration of a tree over a house"></div>

  <div class="person">
    <p class="person__name">Dana <strong>Welk</strong></p>
    <p class="person__role">Owner</p>
  </div>

  <div class="contact contact--address">
    <div class="contact__row">
      <svg class="contact__icon" viewBox="0 0 10 10"><path d="M5 9.5C2.5 6.5 1.8 5 1.8 3.7a3.2 3.2 0 0 1 6.4 0C8.2 5 7.5 6.5 5 9.5z"/><circle cx="5" cy="3.7" r="1.1"/></svg>
      <span>218 Pryor Meadow Lane</span>
    </div>
    <div class="contact__indent">Batesburg, SC 29041</div>
  </div>

  <div class="contact contact--lines">
    <div class="contact__row">
      <svg class="contact__icon" viewBox="0 0 10 10"><path d="M2 1l2 .2.6 2-1.2.9a6 6 0 0 0 2.5 2.5l.9-1.2 2 .6L9 8 7.8 9C4 8.6 1.4 6 1 2.2z"/></svg>
      <span>704.552.1830</span>
    </div>
    <div class="contact__row">
      <svg class="contact__icon" viewBox="0 0 10 10"><rect x="2.5" y="0.8" width="5" height="8.4" rx="0.8"/></svg>
      <span>912.648.2071</span>
    </div>
    <div class="contact__row">
      <svg class="contact__icon contact__icon--solid" viewBox="0 0 10 10"><path d="M1 2.5h8v5H1z"/></svg>
      <span>brightferncustomhomes@mailbox.example</span>
    </div>
    <div class="contact__row">
      <svg class="contact__icon" viewBox="0 0 10 10"><circle cx="5" cy="5" r="3.8"/><path d="M1.2 5h7.6M5 1.2c-2 2.5-2 5 0 7.6M5 1.2c2 2.5 2 5 0 7.6"/></svg>
      <span>www.brightferncustomhomes.example</span>
    </div>
  </div>
</section>

</body>
</html>
```